Window perforation for our storefront

I would like a design for my storefront that houses 2 businesses. The two businesses are similar in that they perform the same operations - audiology (hearing test and hearing aids sales)and Ear, Nose and Throat surgery center. Here are the two website if you need to reference them. https://sonarwellva.com and also https://www.drvantorel.com/
There are 3 window perforations for 3 windows.
PLEASE PAY ATTENTION TO THE SIZE SO THAT RESOLUTION WILL BE HIGH ENOUGH.
The sizes of the windows are as follows: 2 windows at the size of 81"H X 49"W.
The center door is: 30"X 75 1/2"
Left window would have Quiet Meadow Mobile Hearing Aid Center
Right window would have: Vantorel Hearing Aid Center.
Middle window would have store hours. Mon - Thursday 9-5 Friday 9-1
These window perforations will serve to keep the heat out of the office as well as representing the audiology clinic. Please design something that is welcoming, dignified and businesslike - however something that is warm and friendly.

Low design quality

We are a dual Audiology and ENT medical practice. We are looking for something that is professional and on par with the type of services we offer. It needs to be concise so that people can instantly identify who we are and what we do. However we do not wants pictures of the products ( hearings, charging stations, etc.)

Also please do not cut and paste from our website, we can do that and several of the designs we received had just that. There needs to be continuity from one panel to the next.

We are located in the Blue Ridge Mountains of Virginia. Perhaps some imagery of these along the bottom of all three to tie them together. I went to google and entered blue ridge mountain images and the first photo has a beautiful multi colored picture from Pixelgrove that would work well. Anything along those lines that are warm and inviting

Most of the results so far have been loud and pushy that look more like used car advertising rather than a medical clinic. We want to engender trust and portray a professional appearance.

Target Market(s)

All ages. People come to us to restore their hearing. They are aleady sad and frustrated so we are here to make them happy again, to help them hear life and sounds again.

Industry/Entity Type

Audiology and Ear, Nose and Through Doctors

Colors
0054AA
0677BA
7BADD7
CADEEF
E8F1F8
0094D4
00A9DD
6FCCEA
C7EBF8
E9F6FB
00AB8E
00BBA5
67D7C9
C6EFE9
E9F9F6
59FF00
82FF00
B8FF75
E3FFCB
F4FFEA
FFF300
FFF600
FEFA6F
FFFEC7
FFFEE8
FFC000
F8CF3A
FAE287
FDF2CF
FEFAEE
F0912C
F2A743
F7CA91
FBE8D2
FDF5EE
EE7325
F08F49
F5BC92
FAE3D3
FDF4ED

Requirements
Must have
• Continuity. The imagery must flow from one window to another window.
Nice to have
• Use calming and relaxing imagery for the background. You can be free to create something, You can use pictures of landscapes, mountains or anything that is pleasant and gives the person lookin a relaxed feeling.
Should not have
• DO NOT COPY AND PASTE FROM OUR WEBSITES. Do not use hearing aid pictures or people in the design.

```html
<!DOCTYPE html>
<html lang="en">
<head>
<meta charset="utf-8">
<title>Quiet Meadow &amp; Vantorel – Window Perforations</title>
<link rel="stylesheet" href="https://fonts.googleapis.com/css2?family=Montserrat:wght@300;400;500;600&display=swap">
<style>
  :root {
    --canvas: #eceae6;
    --ink: #e0854a;
    --sky-top: #fffdf3;
    --sky-cream: #fdf0c8;
    --sky-gold: #fbd98a;
    --sky-amber: #f8c07a;
    --sky-pink: #f59a8c;
    --haze: #9cc6e6;
    --ridge-light: #3aa6dc;
    --ridge-mid: #1b7fc0;
    --ridge-deep: #0f4f8e;
    --ridge-dark: #0b2f5c;
  }
  * { box-sizing: border-box; margin: 0; padding: 0; }
  html, body { width: 1200px; height: 937px; overflow: hidden; }
  body {
    background: var(--canvas);
    font-family: "Montserrat", sans-serif;
    color: var(--ink);
    position: relative;
  }
  .storefront {
    position: absolute;
    left: 17px;
    bottom: 112px;
    display: flex;
    align-items: flex-end;
    gap: 20px;
  }
  .panel {
    position: relative;
    overflow: hidden;
    background: linear-gradient(to bottom,
      var(--sky-top) 0%,
      var(--sky-cream) 16%,
      var(--sky-gold) 32%,
      var(--sky-amber) 42%,
      var(--sky-pink) 49%,
      var(--haze) 55%,
      var(--haze) 100%);
  }
  .panel--window { width: 431px; height: 713px; }
  .panel--door { width: 264px; height: 664px; }
  .ridges {
    position: absolute;
    left: 0; right: 0; bottom: 0;
    height: 46%;
    background: linear-gradient(to bottom,
      var(--haze) 0%,
      var(--ridge-light) 18%,
      var(--ridge-mid) 42%,
      var(--ridge-deep) 68%,
      var(--ridge-dark) 100%);
  }
  .business-name {
    position: absolute;
    left: 0; right: 0;
    text-align: center;
    line-height: 1.08;
  }
  .business-name__brand { display: block; font-weight: 600; }
  .business-name__line { display: block; font-weight: 300; }
  .business-name--left { top: 96px; }
  .business-name--left .business-name__brand { font-size: 33px; margin-bottom: 2px; }
  .business-name--left .business-name__line { font-size: 41px; }
  .business-name--right { top: 120px; }
  .business-name--right .business-name__brand { font-size: 38px; margin-bottom: 8px; }
  .business-name--right .business-name__line { font-size: 39px; }
  .hours {
    position: absolute;
    top: 56px;
    left: 36px;
    width: 194px;
    border: 1.5px solid var(--ink);
    border-radius: 10px;
    padding: 4px 0 30px;
    text-align: center;
    font-weight: 400;
  }
  .hours legend {
    margin: 0 auto;
    padding: 0 6px;
    font-size: 25px;
    font-weight: 600;
  }
  .hours__day { font-size: 21px; margin-top: 10px; }
  .hours__time { font-size: 21px; margin-top: 4px; }
  .hours__day--friday { margin-top: 22px; }
</style>
</head>
<body>
  <main class="storefront">
    <section class="panel panel--window">
      <h1 class="business-name business-name--left">
        <span class="business-name__brand">Quiet Meadow</span>
        <span class="business-name__line">Mobile Hearing</span>
        <span class="business-name__line">Aid Center</span>
      </h1>
      <div class="ridges" role="img" aria-label="Layered misty Blue Ridge mountain ridges at sunrise"></div>
    </section>

    <section class="panel panel--door">
      <fieldset class="hours">
        <legend>Store hours</legend>
        <p class="hours__day">Mon - Thursday</p>
        <p class="hours__time">9 am-5 am</p>
        <p class="hours__day hours__day--friday">Friday</p>
        <p class="hours__time">9 am-1 am</p>
      </fieldset>
      <div class="ridges" role="img" aria-label="Continuation of the misty Blue Ridge mountain ridges"></div>
    </section>

    <section class="panel panel--window">
      <h1 class="business-name business-name--right">
        <span class="business-name__brand">Vantorel Hearing</span>
        <span class="business-name__line">Aid Center</span>
      </h1>
      <div class="ridges" role="img" aria-label="Blue Ridge mountain ridges fading into morning mist"></div>
    </section>
  </main>
</body>
</html>
```